Tambrook copiers needs flyer for the Corvane Trade expo

A flyer to hand out had the Corvane Trade expo in Melbourne. I am am happy with the layout attached , but i need a claen ( no watermarks) background for the top half of the fist page. It must have one of the copiers attached in the photo

```html
<!DOCTYPE html>
<html lang="en">
<head>
<meta charset="utf-8">
<title>Tambrook copiers – Corvane Trade expo flyer</title>
<link rel="stylesheet" href="https://fonts.googleapis.com/css2?family=Montserrat:wght@400;500;600;700;800&display=swap">
<style>
  :root {
    --red: #ec1c24;
    --red-dark: #a3161b;
    --orange: #ea5d3c;
    --ink: #151515;
    --white: #ffffff;
    --photo-light: #f0f0f0;
    --photo-mid: #b9b9b9;
    --photo-dark: #5e5e5e;
    --machine-light: #eceef1;
    --machine-mid: #d3d6db;
    --machine-blue: #3d4f6e;
  }
  * { margin: 0; padding: 0; box-sizing: border-box; }
  html, body { width: 1200px; height: 744px; overflow: hidden; background: var(--white); }
  body { font-family: "Montserrat", Arial, sans-serif; color: var(--ink); }
  .canvas { position: relative; width: 1200px; height: 744px; }
  .page { position: absolute; top: 0; width: 570px; height: 744px; overflow: hidden; background: var(--white); }
  .page--front { left: 0; }
  .page--back { left: 630px; }
  .page svg.bg { position: absolute; inset: 0; }
  .abs { position: absolute; }

  .hero-photo { left: 0; top: 0; width: 570px; height: 384px;
    background: linear-gradient(165deg, var(--photo-light) 0%, var(--photo-mid) 55%, var(--photo-dark) 100%); }
  .hero-copier { left: 170px; top: 232px; width: 400px; height: 152px;
    background: linear-gradient(180deg, var(--machine-light) 0%, var(--machine-mid) 45%, #8d9096 100%);
    border-top-left-radius: 10px; }
  .hero-copier-panel { left: 205px; top: 246px; width: 110px; height: 34px; background: #3b3e44; border-radius: 3px; }

  .brand { left: 38px; top: 32px; font-weight: 800; font-size: 34px; line-height: 0.95; color: var(--ink); text-transform: uppercase; letter-spacing: -0.5px; }

  .promo-box { left: 299px; top: 103px; width: 271px; height: 133px; background: var(--orange); opacity: 0.95; color: var(--white); padding: 14px 0 0 28px; }
  .promo-box h2 { font-size: 21px; font-weight: 700; line-height: 1.05; }
  .promo-box ul { list-style: none; margin-top: 10px; font-size: 11.5px; line-height: 1.3; }

  .pricing-title { left: 0; width: 570px; top: 397px; text-align: center; color: var(--red); font-size: 16.5px; font-weight: 600; letter-spacing: 0.3px; }
  .rule { height: 1px; background: #cfcfcf; }
  .plan { top: 454px; width: 170px; }
  .plan h3 { color: var(--red); font-size: 11.5px; font-weight: 700; text-align: center; }
  .plan .price { color: var(--red); font-size: 9px; font-weight: 600; text-align: center; margin-top: 6px; line-height: 1.25; }
  .plan .note { color: var(--red); font-size: 6px; font-weight: 600; text-align: center; margin-top: 2px; }
  .plan .price-rule { width: 125px; height: 1px; background: #cfcfcf; margin: 6px auto 0; }
  .plan ul { list-style: none; font-size: 7.5px; font-weight: 500; margin-top: 6px; }
  .plan li { margin-bottom: 20px; line-height: 1.25; }
  .col-divider { width: 1px; background: #cfcfcf; top: 457px; height: 140px; }

  .contact { left: 28px; top: 688px; color: var(--white); font-size: 9.2px; font-weight: 700; }
  .contact span { font-weight: 500; }

  .machine { background: linear-gradient(180deg, var(--machine-blue) 0 12%, var(--machine-light) 12% 100%); border-radius: 4px; }

  .feature-top { left: 276px; top: 36px; color: var(--white); }
  .feature-top h2 { font-size: 19px; font-weight: 700; letter-spacing: 0.3px; }
  .feature-top .rule-w { width: 165px; height: 1px; background: var(--white); margin: 15px 0 13px; }
  .feature-top p { font-size: 15px; line-height: 1.4; padding-left: 2px; }

  .feature-mid { left: 42px; top: 386px; color: var(--white); }
  .feature-mid p { font-size: 13px; font-weight: 500; line-height: 1.3; }
  .feature-mid .gap { margin-top: 16px; }
  .feature-mid .rule-w { width: 168px; height: 1px; background: var(--white); margin: 10px 0 8px; }
  .feature-mid strong { display: block; font-size: 17.5px; font-weight: 700; line-height: 1.35; }
  .feature-mid strong em { font-style: normal; font-size: 20px; }

  .caption { left: 0; width: 570px; top: 668px; text-align: center; color: var(--white); font-size: 10.3px; font-weight: 700; line-height: 1.3; }
</style>
</head>
<body>
<div class="canvas">

  <!-- Front page -->
  <section class="page page--front">
    <div class="abs hero-photo" role="img" aria-label="Black and white photo of hands lifting a sheet of paper from a copier output tray"></div>
    <div class="abs hero-copier" role="img" aria-label="Photo of the freestanding A3 colour copier with its output tray and control panel"></div>
    <div class="abs hero-copier-panel" aria-hidden="true"></div>

    <svg class="bg" width="570" height="744" viewBox="0 0 570 744" aria-hidden="true">
      <path d="M0,222 Q280,300 570,372 L570,388 Q300,372 0,380 Z" fill="var(--red)"/>
      <path d="M380,352 Q480,362 570,372 L570,388 Q480,378 380,368 Z" fill="var(--red-dark)"/>
      <path d="M0,380 Q300,372 570,388 L570,744 L0,744 Z" fill="var(--white)"/>
      <path d="M0,612 Q300,650 570,572 L570,744 L0,744 Z" fill="var(--red-dark)"/>
      <path d="M0,632 Q280,700 570,590 L570,744 L0,744 Z" fill="var(--red)"/>
    </svg>

    <div class="abs brand">Tambrook<br>copiers</div>

    <div class="abs promo-box">
      <h2>NO LOCK-IN<br>CONTRACTS</h2>
      <ul>
        <li>- Freestanding A3 / A4 Colour Printer</li>
        <li>- Change plans to suit your needs</li>
        <li>- Includes All Toner &amp; Service</li>
      </ul>
    </div>

    <h1 class="abs pricing-title">COMPETITIVE PRICING TO SUIT YOUR NEEDS</h1>
    <div class="abs rule" style="left:150px;top:427px;width:272px"></div>

    <div class="abs plan" style="left:14px">
      <h3>SMALL BUSINESS PLAN</h3>
      <p class="price">$150.00 +GST / month<br>or $5.00 +GST / day</p>
      <div class="price-rule"></div>
      <ul>
        <li>- Includes printer &amp; 3000 B&amp;W<br>&nbsp;&nbsp;pages p/m</li>
        <li>- Excess B&amp;W pages are 5c</li>
        <li>- +GST and colour pages are 9c</li>
        <li>+GST</li>
      </ul>
    </div>
    <div class="abs col-divider" style="left:184px"></div>
    <div class="abs plan" style="left:203px">
      <h3>MEDIUM BUSINESS PLAN</h3>
      <p class="price">$210.00 +GST / month<br>or $7.00 +GST / day</p>
      <div class="price-rule"></div>
      <ul>
        <li>- Includes printer &amp; 6000 B&amp;W<br>&nbsp;&nbsp;pages p/m</li>
        <li>- Excess B&amp;W pages are 3.5c</li>
        <li>- +GST and colour pages are 9c</li>
        <li>+GST</li>
      </ul>
    </div>
    <div class="abs col-divider" style="left:373px"></div>
    <div class="abs plan" style="left:386px">
      <h3>DISCOUNT COLOUR PLAN</h3>
      <p class="note">* DISCOUNTS FOR HIGH VOLUME USERS *</p>
      <p class="price">$280.00 +GST / month<br>or Less then $9.50 +GST / day</p>
      <div class="price-rule"></div>
      <ul>
        <li>- Includes printer &amp; 4000 B&amp;W<br>&nbsp;&nbsp;pages p/m</li>
        <li>- Excess B&amp;W pages are 7c</li>
        <li>+GST</li>
      </ul>
    </div>

    <p class="abs contact">GET IN TOUCH WITH US: <span>Call 1800 48 27 19 or visit www.tambrookcopiers.com.au and quote Corvane Trade expo</span></p>
  </section>

  <!-- Back page -->
  <section class="page page--back">
    <svg class="bg" width="570" height="744" viewBox="0 0 570 744" aria-hidden="true">
      <path d="M250,0 L570,0 L570,152 Q430,185 320,168 Q245,150 248,70 Z" fill="var(--red)"/>
      <path d="M0,232 L198,172 L30,345 Z" fill="var(--red)"/>
      <path d="M0,232 L198,172 L0,300 Z" fill="var(--red-dark)"/>
      <path d="M215,300 L570,168 L570,230 Z" fill="var(--red)"/>
      <path d="M215,300 L570,205 L570,230 Z" fill="var(--red-dark)"/>
      <path d="M0,358 L235,358 Q285,358 285,408 L285,508 Q285,558 235,558 L0,558 Z" fill="var(--red)"/>
      <path d="M0,565 Q220,650 570,610 L570,744 L0,744 Z" fill="var(--red-dark)"/>
      <path d="M0,585 Q220,670 570,628 L570,744 L0,744 Z" fill="var(--red)"/>
    </svg>

    <div class="abs machine" style="left:38px;top:28px;width:125px;height:215px" role="img" aria-label="Photo of a freestanding A3 colour multifunction copier"></div>
    <div class="abs machine" style="left:305px;top:355px;width:250px;height:245px" role="img" aria-label="Photo of a colour multifunction copier with finisher unit for stapling and booklet making"></div>

    <div class="abs feature-top">
      <h2>NO LOCK-IN CONTRACT</h2>
      <div class="rule-w"></div>
      <p>Free Network Assistance<br>A3 Printing &amp; Scanning</p>
    </div>

    <div class="abs feature-mid">
      <p>FAX, HOLE PUNCH<br>&amp; STAPLER OPTIONS</p>
      <p class="gap">BOOKLET MAKING</p>
      <div class="rule-w"></div>
      <strong>ALL THIS FROM AS<br>LITTLE AS <em>$5.00 A DAY</em></strong>
    </div>

    <p class="abs caption">OTHER PLANS &nbsp;AVAILABLE FOR TV &amp; MOVIE PRODUCTION COMPANIES,<br>SCHOOLS &amp; CONSTRUCTION SITES, CONTRACT US FOR MORE INFORMATION</p>
  </section>

</div>
</body>
</html>
```